Sermon Series for a church.

Lantern on the Ridge
Sermon Series Nov. 4-18

I have included a sample of making a play on the "art" word in Heart. This is a financial sermon series.

I would like social media posts size of it 1080x1080, full-size 1920x180, and facebook fan page cover photo.

```html
<!DOCTYPE html>
<html lang="en">
<head>
<meta charset="utf-8">
<title>Lantern on the Ridge – Sermon Series Set</title>
<link rel="stylesheet" href="https://fonts.googleapis.com/css2?family=Tenor+Sans&display=swap">
<style>
  :root {
    --canvas: #ffffff;
    --frame: #a8a8a8;
    --ink: #111111;
    --violet: #4b0ea3;
    --purple: #7412b8;
    --magenta: #a712c4;
    --white: #ffffff;
  }
  * { box-sizing: border-box; margin: 0; padding: 0; }
  html, body {
    width: 1200px;
    height: 848px;
    overflow: hidden;
    background: var(--canvas);
    font-family: "Tenor Sans", sans-serif;
    color: var(--ink);
  }
  .board { position: relative; width: 1200px; height: 848px; }

  .piece {
    position: absolute;
    background: var(--canvas);
    border: 1px solid var(--frame);
    overflow: hidden;
  }
  .series-label, .series-date {
    position: absolute;
    text-transform: uppercase;
    letter-spacing: 0.16em;
    white-space: nowrap;
  }

  .paint-mark {
    position: absolute;
    border-radius: 50%;
    background: radial-gradient(circle at 62% 55%, var(--magenta) 0%, var(--purple) 55%, var(--violet) 100%);
    display: flex;
    flex-direction: column;
    align-items: center;
    justify-content: center;
    color: var(--white);
    text-align: center;
    line-height: 1.05;
  }
  .paint-mark .word-major { font-size: 1.5em; }
  .paint-mark .word-minor { font-size: 0.7em; letter-spacing: 0.12em; text-transform: uppercase; }

  /* Square social post */
  .post-square { left: 441px; top: 46px; width: 335px; height: 332px; }
  .post-square .series-label { top: 14px; left: 0; width: 100%; text-align: center; font-size: 21px; }
  .post-square .series-date { top: 292px; left: 0; width: 100%; text-align: center; font-size: 21px; letter-spacing: 0.08em; }
  .post-square .paint-mark { left: 50px; top: 70px; width: 196px; height: 196px; font-size: 24px; }

  /* Wide web banner */
  .banner-wide { left: 235px; top: 409px; width: 731px; height: 68px; }
  .banner-wide .paint-band {
    position: absolute; left: 40px; top: 0; width: 320px; height: 68px;
    background: linear-gradient(90deg, var(--violet) 0%, var(--purple) 45%, var(--magenta) 100%);
    border-radius: 0 40px 40px 0;
    display: flex; align-items: center; justify-content: center;
    color: var(--white); font-size: 24px; letter-spacing: 0.02em;
  }
  .banner-wide .series-label { left: 383px; top: 24px; font-size: 17px; }
  .banner-wide .series-date { left: 604px; top: 24px; font-size: 17px; letter-spacing: 0.08em; }

  /* Page cover */
  .cover-wide { left: 233px; top: 505px; width: 732px; height: 236px; }
  .cover-wide .paint-field {
    position: absolute; left: 0; top: 0; width: 260px; height: 236px;
    background: linear-gradient(115deg, var(--magenta) 0%, var(--purple) 45%, rgba(75,14,163,0.55) 75%, rgba(255,255,255,0) 100%);
  }
  .cover-wide .series-label { left: 161px; top: 26px; font-size: 19px; }
  .cover-wide .series-date { left: 211px; top: 57px; font-size: 17px; letter-spacing: 0.08em; }
  .cover-wide .paint-mark { left: 437px; top: 10px; width: 206px; height: 206px; font-size: 25px; }

  .profile-slot {
    position: absolute; left: 282px; top: 650px; width: 152px; height: 150px;
    background: var(--canvas); border: 1px solid var(--frame);
  }
</style>
</head>
<body>
<main class="board">

  <section class="piece post-square">
    <p class="series-label">Sermon Series</p>
    <div class="paint-mark" role="img" aria-label="Purple paint-splash circle artwork with series title">
      <span class="word-major">Lantern</span>
      <span class="word-minor">on the</span>
      <span class="word-major">Ridge</span>
    </div>
    <p class="series-date">Nov. 4-18</p>
  </section>

  <section class="piece banner-wide">
    <div class="paint-band" role="img" aria-label="Purple paint-splash band artwork with series title">Lantern on the Ridge</div>
    <p class="series-label">Sermon Series</p>
    <p class="series-date">Nov. 4-18</p>
  </section>

  <section class="piece cover-wide">
    <div class="paint-field" role="img" aria-label="Purple and violet paint splatter artwork"></div>
    <p class="series-label">Sermon Series</p>
    <p class="series-date">Nov. 4-18</p>
    <div class="paint-mark" role="img" aria-label="Purple paint-splash circle artwork with series title">
      <span class="word-major">Lantern</span>
      <span class="word-minor">on the</span>
      <span class="word-major">Ridge</span>
    </div>
  </section>

  <div class="profile-slot" aria-label="Profile picture area"></div>

</main>
</body>
</html>
```